LinkedIn header in combination with existing logo

The header of the LinkedIn profile% 26quot; https: //www.brelvonet.com/company/dacomeadvisory%26quot; shall be renewed. Therefore, a new background image shall be designed. A design is simple, clear, well structured and fits the consulting business. This article should be used as a separate project for publications. It will become the corporate identity for social media and employer branding. In case you have any questions, feel free to contact us.b ***************** * Background *: DACOME is a leading international management consultancy for operations. With unique concepts and the right employees, we achieve effective results. We support well-known companies from industry and trade in the optimization of the total value-added chain all over the world. Our custom-tailored approach enables us to quickly optimize our customer's processes along the value-added chain. Dacome works in the following branches: - Automotive / Automotive supplier - Pharmaceutical - Foundry - Shipyard - Steel industry - Consumer goods - Energy - Engineering - Electronics - Facility engineering% 26amp; construction

Target Market(s)

Consulting / Industry (Pharmaceutical, productive industry, metal, shipbuilding, automotive)

Industry/Entity Type

Management Consulting

Font styles to use
Other font styles liked:
• see PPT

Colors

Designer to choose colors to be used in the design.

Requirements
Must have
• Please follow the recommended LinkedIn resolution guideline (see also: LinkedIn_Guideline.jpg). Rectangular background (see page 26) top_picks_advisory% 26quot; top_picks_advisory% 26quot;, three sizes next to each other) right.
Nice to have
• PowerPoint presentation as a guideline however, not as a must have in case you want to use images. You want to find various available licensed pictures. These can be used, but we believe that a simple and neutral (abstract?) Background image would be better. - 26gt%; You are also considered if you do not use one of the provided pictures at all! We want to test a simplistic design as well. Convince us!

```html
<!DOCTYPE html>
<html lang="en">
<head>
<meta charset="utf-8">
<title>Dacome Management Consulting – Social Header</title>
<link rel="stylesheet" href="https://fonts.googleapis.com/css2?family=Open+Sans:wght@400;600&display=swap">
<style>
  :root {
    --page-bg: #ffffff;
    --brand-red: #b01a2e;
    --brand-red-bright: #d8203a;
    --charcoal: #231f22;
    --wordmark: #e4e6ea;
    --tagline: #d6cfd0;
    --photo-blue: #4a5a78;
    --text-light: #ffffff;
  }
  * { margin: 0; padding: 0; box-sizing: border-box; }
  html, body {
    width: 1200px; height: 1200px; overflow: hidden;
    background: var(--page-bg);
    font-family: "Open Sans", "Segoe UI", sans-serif;
  }
  .header-banner {
    position: absolute;
    left: 34px; top: 428px;
    width: 1132px; height: 344px;
    overflow: hidden;
  }
  .meeting-photo {
    position: absolute; left: 0; top: 0;
    width: 769px; height: 100%;
    background:
      radial-gradient(ellipse at 45% 75%, rgba(200,204,210,0.9) 0%, rgba(200,204,210,0) 45%),
      radial-gradient(ellipse at 85% 40%, rgba(220,200,190,0.5) 0%, rgba(220,200,190,0) 30%),
      linear-gradient(100deg, #b9c0cc 0%, var(--photo-blue) 18%, #3c4866 45%, #2a2f40 75%, #1f2230 100%);
  }
  .brand-band {
    position: absolute; left: 0; top: 0;
    width: 769px; height: 81px;
    background: linear-gradient(90deg, rgba(200,40,60,0.9) 0%, rgba(150,50,55,0.85) 30%, rgba(60,45,45,0.85) 60%, rgba(40,36,38,0.9) 100%);
  }
  .brand-name {
    position: absolute; left: 96px; top: 10px;
    font-size: 40px; line-height: 1; font-weight: 600; letter-spacing: 1px;
    color: var(--wordmark);
  }
  .brand-tagline {
    position: absolute; left: 180px; top: 52px;
    font-size: 18px; line-height: 1; font-weight: 400;
    color: var(--tagline);
  }
  .branches-panel {
    position: absolute; left: 769px; top: 0;
    width: 363px; height: 100%;
    background: linear-gradient(90deg, var(--brand-red) 0%, #b02838 18%, #6a2a32 45%, #2e2528 70%, var(--charcoal) 100%);
    color: var(--text-light);
  }
  .branch-list {
    list-style: none;
    position: absolute; left: 27px; top: 40px;
    font-size: 19.5px; line-height: 23.8px; white-space: nowrap;
  }
  .branch-list li::before { content: "- "; }
  .panel-mark {
    position: absolute; right: 14px; bottom: 14px;
    font-size: 17px; font-weight: 600;
    color: var(--brand-red-bright);
  }
</style>
</head>
<body>
  <section class="header-banner">
    <div class="meeting-photo" role="img" aria-label="Business meeting at an office table with a handshake, a potted plant and a coffee cup"></div>
    <div class="brand-band">
      <div class="brand-name">DACOME</div>
      <div class="brand-tagline">Management Consulting</div>
    </div>
    <aside class="branches-panel">
      <ul class="branch-list">
        <li>Automotive / Automotive supplier</li>
        <li>Pharmaceutical</li>
        <li>Foundry</li>
        <li>Shipyards</li>
        <li>Steel industry</li>
        <li>Consumer goods</li>
        <li>Energy</li>
        <li>Engineering</li>
        <li>Electronics</li>
        <li>Facility engineering construction</li>
      </ul>
      <div class="panel-mark">DACOME</div>
    </aside>
  </section>
</body>
</html>
```